Cool modern, tech Business card design

Looking for a new business card design for our Managed IT Services company. We would like 2 sides, with the logo one one side horizontally and then the information on the back in either vertical or horizontal. We want our colors from the logo incorporated but also would like to see the color gray in there as well.

Target Market(s)

IT, Information Technology, Tech, Service

Industry/Entity Type

It Service

Contact Information for Business Card

Carl Penner
Managing Partner
(P)555-271-4830 ext xxx
(F)555-271-4831
www.brixtelcore.com

Font styles to use
Sans Serif

Colors
959595
000000
ec1f27

Requirements
Must have
• Logo on one side with some nice design or pattern
• Information on back in either vertical or horizontal format
Nice to have
• For it to look cool, tech, modern, stand out.

```html
<!DOCTYPE html>
<html lang="en">
<head>
<meta charset="utf-8">
<title>Brixtelcore Business Card</title>
<link rel="stylesheet" href="https://fonts.googleapis.com/css2?family=Ubuntu:wght@400;500;700&display=swap">
<style>
  :root {
    --backdrop: #b4b4b4;
    --card: #f1f1f1;
    --ink: #1a1a1a;
    --red: #b01e2c;
    --black: #111111;
    --gray: #959595;
  }
  * { margin: 0; padding: 0; box-sizing: border-box; }
  html, body {
    width: 1200px; height: 576px; overflow: hidden;
    background: var(--backdrop);
    font-family: "Ubuntu", sans-serif;
    color: var(--ink);
  }
  .canvas { position: relative; width: 1200px; height: 576px; }

  .card {
    position: absolute;
    top: 138px;
    height: 294px;
    background: var(--card);
    border-radius: 14px;
    overflow: hidden;
    box-shadow: 0 2px 6px rgba(0,0,0,0.25);
  }

  .wordmark { font-weight: 500; color: var(--black); letter-spacing: -0.5px; line-height: 1; white-space: nowrap; }

  /* Front */
  .card-front { left: 82px; width: 484px; }
  .front-brand {
    position: absolute; left: 0; right: 0; top: 146px;
    text-align: center;
  }
  .front-brand .wordmark { font-size: 46px; }
  .front-url {
    position: absolute; left: 0; right: 0; top: 254px;
    text-align: center; font-size: 12px; font-weight: 500;
  }
  .front-band { position: absolute; left: 0; right: 0; bottom: 0; height: 13px; display: flex; }
  .front-band .band-black { flex: 1; background: var(--black); }
  .front-band .band-red { flex: 1; background: var(--red); }

  /* Back */
  .card-back { left: 602px; width: 482px; }
  .side-band { position: absolute; left: 0; top: 0; bottom: 0; width: 42px; background: var(--red); }
  .side-rule { position: absolute; left: 42px; top: 0; bottom: 0; width: 2px; background: var(--black); }
  .person { position: absolute; left: 64px; top: 44px; }
  .person-name { font-size: 19px; font-weight: 700; color: var(--red); }
  .person-title { font-size: 12.5px; margin-top: 5px; }
  .back-brand { position: absolute; right: 24px; top: 90px; }
  .back-brand .wordmark { font-size: 28px; }
  .contact { position: absolute; left: 64px; top: 187px; list-style: none; font-size: 12px; }
  .contact li { display: flex; align-items: center; height: 17px; }
  .contact svg { width: 11px; height: 11px; margin: 0 10px 0 4px; fill: var(--red); }
  .contact .address { margin-top: 3px; }
</style>
</head>
<body>
<div class="canvas">

  <section class="card card-front">
    <div class="front-brand">
      <span class="wordmark">brixtelcore</span>
    </div>
    <p class="front-url">www.brixtelcore.com</p>
    <div class="front-band"><span class="band-black"></span><span class="band-red"></span></div>
  </section>

  <section class="card card-back">
    <div class="side-band"></div>
    <div class="side-rule"></div>
    <div class="person">
      <p class="person-name">Carl Penner</p>
      <p class="person-title">Managing Partner</p>
    </div>
    <div class="back-brand">
      <span class="wordmark">brixtelcore</span>
    </div>
    <ul class="contact">
      <li><svg viewBox="0 0 12 12"><path d="M1 3c0-1 1-2 5-2s5 1 5 2v1H8V3H4v1H1z M3 5h6l2 5H1z"/></svg>555-271-4830 ext xxx</li>
      <li><svg viewBox="0 0 12 12"><path d="M1 3c0-1 1-2 5-2s5 1 5 2v1H8V3H4v1H1z M3 5h6l2 5H1z"/></svg>555-271-4831</li>
      <li><svg viewBox="0 0 12 12"><path d="M1 2h10v8H1z" /><path d="M1 2l5 4 5-4" fill="none" stroke="#f1f1f1" stroke-width="1"/></svg>carl@brixtelcore.com</li>
      <li><svg viewBox="0 0 12 12"><circle cx="6" cy="6" r="5"/><path d="M1 6h10M6 1c-2 3-2 7 0 10M6 1c2 3 2 7 0 10" fill="none" stroke="#f1f1f1" stroke-width="0.8"/></svg>www.brixtelcore.com</li>
      <li class="address">42 Alder Lane Westbury, New York 11590</li>
    </ul>
  </section>

</div>
</body>
</html>
```